Bref créative |
BrightMoor Guard, LLC. | ||
Use standard fonts | ||
Cutting-Edge Modern Simple |
Derek Palvane | ||
Master Technician | ||
leave blank | ||
brightmooritllc@quellmail.example | ||
http://brightmoorguard.example | ||

```html
<!DOCTYPE html>
<html lang="en">
<head>
<meta charset="utf-8">
<title>BrightMoor Guard, LLC. Stationery</title>
<link href="https://fonts.googleapis.com/css2?family=Cinzel:wght@400;600&family=Lato:wght@400;700&display=swap" rel="stylesheet">
<style>
  :root {
    --backdrop: #d9dadc;
    --paper: #ffffff;
    --ink: #1d1d1f;
    --brand-blue: #2f63b4;
    --brand-blue-dark: #1e4a92;
    --muted: #6b6f76;
    --faint: #e7ecf3;
    --paper-shade: #f4f5f7;
  }
  * { margin: 0; padding: 0; box-sizing: border-box; }
  html, body { width: 1200px; height: 936px; overflow: hidden; }
  body {
    background: var(--backdrop);
    position: relative;
    font-family: 'Lato', Arial, sans-serif;
    color: var(--ink);
  }
  .piece { position: absolute; background: var(--paper); overflow: hidden; }

  .corner-graphic {
    position: absolute; right: 0; bottom: 0;
    background: radial-gradient(circle at 100% 100%,
      rgba(47, 99, 180, 0.55) 0%,
      rgba(30, 74, 146, 0.35) 40%,
      rgba(29, 29, 31, 0.12) 70%,
      rgba(255, 255, 255, 0) 100%);
  }

  .brand-name {
    font-family: 'Cinzel', 'Times New Roman', serif;
    font-weight: 600;
    color: var(--ink);
    letter-spacing: 0.04em;
    white-space: nowrap;
  }
  .brand-dot {
    display: inline-block;
    flex: none;
    border-radius: 50%;
    background: var(--brand-blue);
    vertical-align: middle;
  }

  /* Letterhead */
  .letterhead { left: 178px; top: 63px; width: 395px; height: 655px; }
  .letterhead .masthead { position: absolute; left: 18px; top: 22px; display: flex; align-items: center; gap: 8px; }
  .letterhead .brand-dot { width: 26px; height: 26px; }
  .letterhead .brand-name { font-size: 9px; }
  .letterhead .tagline { font-family: 'Cinzel', serif; font-size: 5.5px; color: var(--muted); letter-spacing: 0.1em; margin-top: 2px; }
  .letterhead .contact {
    position: absolute; left: 222px; top: 26px;
    font-size: 6.5px; line-height: 11px; color: var(--muted);
  }
  .letterhead .contact li { list-style: none; display: flex; align-items: center; gap: 5px; white-space: nowrap; }
  .letterhead .contact i { width: 6px; height: 6px; border-radius: 50%; background: var(--brand-blue); display: inline-block; }
  .letterhead .faint-mark {
    position: absolute; left: 115px; top: 250px; width: 135px; height: 135px;
    border-radius: 50%; background: var(--faint);
  }
  .letterhead .corner-graphic { width: 210px; height: 140px; }

  /* Folder */
  .folder { left: 629px; top: 51px; width: 406px; height: 680px; }
  .folder .identity { position: absolute; left: 0; right: 0; top: 250px; text-align: center; }
  .folder .brand-dot { width: 52px; height: 52px; margin-bottom: 10px; }
  .folder .brand-name { font-size: 17px; display: block; }
  .folder .tagline { font-family: 'Cinzel', serif; font-size: 12px; letter-spacing: 0.06em; margin-top: 4px; }
  .folder .corner-graphic { width: 210px; height: 140px; }

  /* Business cards */
  .card-front { left: 43px; top: 741px; width: 201px; height: 81px; }
  .card-front .corner-graphic {
    left: 0; top: 0; right: auto; bottom: auto; width: 95px; height: 36px;
    background: radial-gradient(circle at 0% 0%,
      rgba(47, 99, 180, 0.5) 0%,
      rgba(29, 29, 31, 0.12) 65%,
      rgba(255, 255, 255, 0) 100%);
  }
  .card-front .mini-brand { position: absolute; left: 10px; top: 44px; display: flex; align-items: center; gap: 4px; }
  .card-front .mini-brand .brand-dot { width: 12px; height: 12px; }
  .card-front .mini-brand .brand-name { font-size: 5.5px; }
  .card-front .details { position: absolute; left: 104px; top: 12px; font-size: 5.5px; line-height: 8.5px; color: var(--muted); white-space: nowrap; }
  .card-front .person { position: absolute; left: 104px; top: 46px; }
  .card-front .person strong { display: block; font-size: 7px; color: var(--ink); }
  .card-front .person span { font-size: 5.5px; color: var(--muted); }

  .card-back {
    left: 43px; top: 837px; width: 201px; height: 81px;
    background: linear-gradient(135deg, var(--brand-blue) 0%, var(--brand-blue-dark) 100%);
    display: flex; align-items: center; justify-content: center;
  }
  .card-back .brand-name { color: var(--paper); font-size: 9px; }

  /* Envelope front */
  .envelope-front { left: 264px; top: 743px; width: 434px; height: 140px; }
  .envelope-front .return-address { position: absolute; left: 14px; top: 14px; display: flex; align-items: center; gap: 6px; }
  .envelope-front .brand-dot { width: 18px; height: 18px; }
  .envelope-front .brand-name { font-size: 7.5px; }
  .envelope-front .tagline { font-family: 'Cinzel', serif; font-size: 5px; color: var(--muted); letter-spacing: 0.1em; margin-top: 1px; }
  .envelope-front .corner-graphic { width: 170px; height: 105px; }

  /* Envelope back */
  .envelope-back { left: 738px; top: 738px; width: 429px; height: 152px; background: var(--paper-shade); }
  .envelope-back .flap {
    position: absolute; left: 0; top: 0; width: 100%; height: 62px;
    background: linear-gradient(180deg, var(--brand-blue) 0%, var(--brand-blue-dark) 100%);
    display: flex; align-items: center; justify-content: center;
  }
  .envelope-back .web { color: var(--paper); font-size: 8px; letter-spacing: 0.35em; }
  .envelope-back .fold { position: absolute; left: 0; top: 62px; width: 100%; height: 90px; }
</style>
</head>
<body>

<section class="piece letterhead" aria-label="Letterhead">
  <header class="masthead">
    <span class="brand-dot"></span>
    <div>
      <div class="brand-name">BrightMoor Guard, LLC.</div>
      <div class="tagline">AN IT SOLUTIONS FIRM</div>
    </div>
  </header>
  <ul class="contact">
    <li><i></i>brightmooritllc@quellmail.example</li>
    <li><i></i>http://brightmoorguard.example</li>
  </ul>
  <div class="faint-mark"></div>
  <div class="corner-graphic" role="img" aria-label="Decorative black and blue curved arcs"></div>
</section>

<section class="piece folder" aria-label="Presentation folder">
  <div class="identity">
    <span class="brand-dot"></span>
    <span class="brand-name">BrightMoor Guard, LLC.</span>
    <div class="tagline">An IT Solutions Firm.</div>
  </div>
  <div class="corner-graphic" role="img" aria-label="Decorative black and blue curved arcs"></div>
</section>

<section class="piece card-front" aria-label="Business card front">
  <div class="corner-graphic" role="img" aria-label="Decorative black and blue curved arcs"></div>
  <div class="mini-brand">
    <span class="brand-dot"></span>
    <span class="brand-name">BrightMoor Guard</span>
  </div>
  <div class="details">
    brightmooritllc@quellmail.example<br>
    http://brightmoorguard.example
  </div>
  <div class="person">
    <strong>Derek Palvane</strong>
    <span>Master Technician</span>
  </div>
</section>

<section class="piece card-back" aria-label="Business card back">
  <span class="brand-name">BrightMoor Guard</span>
</section>

<section class="piece envelope-front" aria-label="Envelope front">
  <div class="return-address">
    <span class="brand-dot"></span>
    <div>
      <div class="brand-name">BrightMoor Guard, LLC.</div>
      <div class="tagline">AN IT SOLUTIONS FIRM</div>
    </div>
  </div>
  <div class="corner-graphic" role="img" aria-label="Decorative black and blue curved arcs"></div>
</section>

<section class="piece envelope-back" aria-label="Envelope back">
  <div class="flap"><span class="web">WWW.BRIGHTMOORGUARD.EXAMPLE</span></div>
  <svg class="fold" viewBox="0 0 429 90" preserveAspectRatio="none" aria-hidden="true">
    <path d="M0,90 L214,20 L429,90" fill="none" stroke="#e2e4e8" stroke-width="1"/>
  </svg>
</section>

</body>
</html>
```